Business Card Design for a Private Label Pet Company

We need a business card design for our family-owned company, Hollow Creek Pet Works (www.hollowcreekpetworks.com), out of St. Louis, MO. We provide turnkey private label solutions for retailers, Marketvale sellers and other brands who want to provide high quality, natural, Made in the USA pet products to their customers. Our customer are worldwide and range from the US to the UK to Vietnam and beyond. We offer private label for dozens of pet products including grooming products (shampoos, conditioners, colognes, ear and eye washes, mouthwash, etc.), all meat treats, supplements, and specialty products (pet stain and odor cleaner, anti-chew spray, etc.). We would like to see designs that use the colors, fonts and logos (see variations) within our brand guidelines and fit with the look and feel from our website.

Target Market(s)

Pet Store Owners, Marketvale Sellers, Pet Brand Marketers

Industry/Entity Type

Pet

Contact Information for Business Card

Tom Willoughby
CEO
Hollow Creek Pet Works
5817 Brookhaven Commerce Lane
St. Louis, MO 63521
office: 314.555.0182
mobile: 770.555.0139
email: tom@hollowcreekpetworks.com

Colors

Designer to choose colors to be used in the design.

Requirements
Must have
• Need to follow the brand guidelines attached for colors, fonts and logos
• Need to use the logos attached (or a variation) with our without the tagline
• Name, title, phone (office and mobil), email, address on the business card
• Clean professional look and feel that says: high quality natural pet products, high quality service, made in the USA
Nice to have
• Made in the USA is a big positive in our industry and we are very proud of it. There is an attached icon from our website. The designer can get creative here as they wish.
• I do like using color for pop. Just don't like lots of bright, loud colors.
Should not have
• lots of bright, loud colors
• overwhelming to the reader
• crowded

```html
<!DOCTYPE html>
<html lang="en">
<head>
<meta charset="utf-8">
<title>Hollow Creek Pet Works – Business Card</title>
<link rel="stylesheet" href="https://fonts.googleapis.com/css2?family=Bebas+Neue&family=Montserrat:wght@400;500;700&display=swap">
<style>
  :root {
    --backdrop: #d9dcdb;
    --card-light: #efefee;
    --pattern-tone: #e2e3e2;
    --slate: #3f5552;
    --slate-panel: #4b6360;
    --charcoal: #2a2a2a;
    --charcoal-deep: #1f1f1f;
    --ink-light: #f4f4f4;
    --rule: #9aa3a1;
  }
  * { box-sizing: border-box; margin: 0; padding: 0; }
  html, body { width: 1200px; height: 1000px; overflow: hidden; }
  body {
    background: var(--backdrop);
    font-family: "Montserrat", sans-serif;
    position: relative;
  }
  .card {
    position: absolute;
    top: 350px;
    width: 525px;
    height: 300px;
    border-radius: 22px;
    overflow: hidden;
    box-shadow: 0 10px 28px rgba(0,0,0,.22);
  }
  /* Front */
  .card-front { left: 50px; background: var(--card-light); }
  .paw-pattern {
    position: absolute; inset: 0;
    background: radial-gradient(circle at 50% 50%, var(--card-light), var(--pattern-tone));
  }
  .front-content {
    position: absolute; inset: 0;
    display: flex; flex-direction: column; align-items: center; justify-content: center;
  }
  .front-wordmark {
    font-family: "Montserrat", sans-serif;
    font-weight: 700;
    font-size: 33px;
    color: var(--slate);
    letter-spacing: .5px;
    text-transform: uppercase;
    text-align: center;
    line-height: 1.15;
  }
  .front-rule { width: 390px; height: 2px; background: var(--rule); margin: 14px 0; }
  .front-tagline {
    font-size: 17px; font-weight: 500; color: var(--slate);
    letter-spacing: .8px; text-transform: uppercase;
  }
  /* Back */
  .card-back { left: 625px; background: var(--charcoal); }
  .back-shapes { position: absolute; inset: 0; }
  .contact {
    position: absolute; left: 30px; top: 36px; color: var(--ink-light);
  }
  .person-name {
    font-family: "Bebas Neue", sans-serif; font-size: 30px; letter-spacing: .6px; line-height: 1;
  }
  .person-title { font-size: 11px; font-weight: 500; margin-top: 2px; }
  .address { font-size: 11.5px; line-height: 1.45; margin-top: 34px; }
  .contact-list { list-style: none; margin-top: 22px; font-size: 11.5px; }
  .contact-list li { display: flex; align-items: center; gap: 8px; line-height: 1.75; }
  .contact-list svg { width: 11px; height: 11px; fill: var(--ink-light); flex: none; }
  .back-wordmark {
    position: absolute; left: 340px; top: 40px; width: 170px;
    font-family: "Montserrat", sans-serif; font-weight: 700; font-size: 17px;
    color: var(--charcoal-deep); text-transform: uppercase; text-align: center; line-height: 1.2;
  }
  .usa-seal {
    position: absolute; left: 378px; top: 178px; width: 96px; height: 96px;
    border-radius: 50%;
    background: radial-gradient(circle, #c9ccd3 0 54%, #5d6d6a 55% 100%);
    border: 2px solid #c9cfcd;
  }
</style>
</head>
<body>
  <section class="card card-front">
    <div class="paw-pattern" role="img" aria-label="Faint repeating paw print pattern"></div>
    <div class="front-content">
      <div class="front-wordmark">Hollow Creek<br>Pet Works</div>
      <div class="front-rule"></div>
      <div class="front-tagline">Turnkey Private Label Partner</div>
    </div>
  </section>

  <section class="card card-back">
    <svg class="back-shapes" viewBox="0 0 525 300" aria-hidden="true">
      <polygon points="336,0 525,0 525,300 316,300" fill="var(--slate-panel)"/>
      <polygon points="336,0 525,0 525,152 327,132" fill="var(--card-light)"/>
      <line x1="327" y1="0" x2="307" y2="300" stroke="#f4f4f4" stroke-width="2"/>
      <line x1="327" y1="140" x2="525" y2="160" stroke="#f4f4f4" stroke-width="1.5"/>
    </svg>
    <div class="contact">
      <div class="person-name">Tom Willoughby</div>
      <div class="person-title">CEO</div>
      <div class="address">5817 Brookhaven Commerce Lane<br>St. Louis, MO 63521</div>
      <ul class="contact-list">
        <li><svg viewBox="0 0 24 24"><path d="M6.6 10.8a15 15 0 0 0 6.6 6.6l2.2-2.2a1 1 0 0 1 1-.25 11.4 11.4 0 0 0 3.6.57 1 1 0 0 1 1 1V20a1 1 0 0 1-1 1A17 17 0 0 1 3 4a1 1 0 0 1 1-1h3.5a1 1 0 0 1 1 1c0 1.25.2 2.45.57 3.57a1 1 0 0 1-.25 1z"/></svg>314.555.0182</li>
        <li><svg viewBox="0 0 24 24"><path d="M7 1h10a2 2 0 0 1 2 2v18a2 2 0 0 1-2 2H7a2 2 0 0 1-2-2V3a2 2 0 0 1 2-2zm0 3v15h10V4z"/></svg>770.555.0139</li>
        <li><svg viewBox="0 0 24 24"><path d="M2 5h20v14H2zm2 2v.5l8 5 8-5V7z"/></svg>tom@hollowcreekpetworks.com</li>
      </ul>
    </div>
    <div class="back-wordmark">Hollow Creek<br>Pet Works</div>
    <div class="usa-seal" role="img" aria-label="Made in the USA seal with flag"></div>
  </section>
</body>
</html>
```